Velmora Swinger site - new website, blogsite and merchandise point, connection to tradevale

We are a well established Swingers Club in the North east of UK and already have an existing site. www.velmora.co.uk, BUT we have changed our logo and our information on the site needs to be updated.

We are changing our hosting site to Nestiply.com ,also wanting to start a blog which is linked to the club, plus we wish to sell a small exclusive range of Velmora linked merchandise which will also be available on Tradevale.

I have attached a pdf of the majority of the content. additionally we will provide pictures and a videoclip which should be able to be viewed by pc's, lap tops and mobile phones (the whole website must be fully accessible via phone).

The new site must be able to be updated by someone with medium computer knowledge (usually me), by no means expert. Updates will generally be new pictures and written information. The site must be able to be transferred to Nestiply.

Velmora is one of the countries leading clubs and emphasises friendliness, fun & safety for its members, we look after you to ensure your experience is the best we can offer. We are very proud of our reputation, built up over more than 10 years.

Target Market(s)

Swingers, dreamers & fantasists, alternative lifestyle people

Coding

Coded - Design and coding required

Number of Pages Required

5+ page

Font styles to use
Sans Serif

Colors
000000
ec1f27
fbfbfb
eeeeee
eaeaea

Requirements
Must have
• website with blog attached, link to tradevale & coinlark, ability to run videoclip and picture album and must be compatable to transfer easily to Nestiply and be updated by non-professional (who can learn)
• Straightforward & easy to navigate
• over 18 content page with enter button
Nice to have
• sexy site
• link to chirpnet maybe
• black site would be nice with red or white writing
Should not have
• children and animals in anyway shape or form

```html
<!DOCTYPE html>
<html lang="en">
<head>
<meta charset="utf-8">
<title>Velmora – Membership</title>
<link href="https://fonts.googleapis.com/css2?family=Marcellus&family=Open+Sans:ital,wght@0,400;0,600;0,700;1,400;1,700&display=swap" rel="stylesheet">
<style>
:root{
  --black:#000000;
  --red:#ec1f27;
  --white:#fbfbfb;
  --grey-1:#eeeeee;
  --grey-2:#eaeaea;
  --ink:#444444;
  --ink-soft:#555555;
  --bar-dark:#333333;
  --bar-mid:#5a5a5a;
  --rule:#b9b9b9;
}
*{margin:0;padding:0;box-sizing:border-box}
html,body{width:1200px;height:2844px;overflow:hidden}
body{font-family:"Open Sans",Arial,sans-serif;color:var(--ink);background:var(--grey-2);position:relative}
a{color:inherit;text-decoration:none}

/* hero */
.hero{position:absolute;left:0;top:0;width:1200px;height:382px;overflow:hidden}
.hero-photo{position:absolute;inset:0;background:
  radial-gradient(ellipse at 62% 40%,rgba(150,140,120,.55),rgba(0,0,0,0) 45%),
  linear-gradient(180deg,#1b2130 0%,#28303e 45%,#3a2f22 78%,#141414 100%)}
.topbar{position:absolute;right:98px;top:14px;font-size:16px;color:var(--white);display:flex;align-items:center;gap:10px}
.topbar .ico{width:15px;height:15px;fill:var(--red)}
.topbar .sep{margin:0 8px}
.logo{position:absolute;left:98px;top:32px;font-family:"Marcellus",serif;font-size:40px;color:var(--white);letter-spacing:1px}
.mainnav{position:absolute;right:98px;top:54px;display:flex;gap:17px;font-size:16px;color:var(--white);align-items:center}
.mainnav .active{color:var(--red)}
.mainnav svg{width:16px;height:16px;fill:none;stroke:var(--white);stroke-width:2.4}
.hero-title{position:absolute;left:0;right:0;top:150px;text-align:center;font-family:"Marcellus",serif;font-size:90px;letter-spacing:22px;color:var(--white)}
.dots{position:absolute;top:329px;left:0;right:0;display:flex;justify-content:center;gap:8px}
.dots span{width:12px;height:12px;border-radius:50%;border:2px solid var(--white)}
.dots span.on{background:var(--white)}

/* main */
.main{position:absolute;left:0;top:382px;width:1200px;height:1584px;background:linear-gradient(180deg,var(--grey-1),#e2e2e2 60%,var(--grey-1))}
.wrap{position:absolute;left:100px;width:1000px}
.crumb{top:12px;font-size:15px;color:#333}
.crumb .cur{color:var(--red)}
.crumb::after{content:"";position:absolute;left:0;right:0;top:35px;border-top:1px solid var(--rule)}
h2{font-family:"Marcellus",serif;font-weight:400;font-size:34px;color:#333;text-align:center}
.intro{top:105px}
.intro p{font-size:12.6px;line-height:24px;text-align:center;color:var(--ink-soft);margin-top:30px}
.intro p:first-of-type{margin-top:34px}
.divider{top:662px;border-top:1px solid var(--rule)}
.fees{top:700px;text-align:center}
.fees .price{font-size:13px;line-height:37px;color:var(--ink-soft);margin-top:16px}
.fees .note{font-style:italic;font-weight:700;font-size:15.5px;line-height:28px;color:#222;margin-top:14px}

.plans{top:976px;display:flex;justify-content:space-between}
.plan{width:310px}
.plan-box{height:316px;border:1px solid #9a9a9a;background:rgba(255,255,255,.25)}
.plan-title{background:var(--bar-dark);color:var(--white);font-weight:700;font-size:19px;text-align:center;height:46px;line-height:46px;text-transform:uppercase}
.plan-time{background:var(--bar-mid);color:var(--white);font-weight:600;font-size:16px;text-align:center;height:34px;line-height:34px}
.plan.featured .plan-title{background:var(--red)}
.plan.featured .plan-time{background:#ef5a5f}
.plan ul{list-style:none;padding:18px 0 0 26px}
.plan li{font-size:14px;color:var(--ink-soft);line-height:36px;display:flex;align-items:center;gap:10px}
.plan li svg{width:14px;height:14px;flex:none}
.plan li.plain{padding-left:24px}
.plan .select{text-align:center;font-size:14px;color:#777;margin-top:12px;margin-bottom:-10px}
.plan-note{font-style:italic;font-size:11.5px;line-height:22px;color:#333;margin-top:14px}
.plan-note + .plan-note{margin-top:22px}

/* contact */
.contact{position:absolute;left:0;top:1966px;width:1200px;height:612px;overflow:hidden;color:var(--white);text-align:center}
.contact-photo{position:absolute;inset:0;background:radial-gradient(ellipse at 30% 40%,#3a3a3a,#151515 70%),#111}
.contact h2{position:relative;color:var(--white);margin-top:64px}
.contact p{position:relative;font-size:13px;line-height:28px;width:710px;margin:34px auto 0}
.contact p:first-of-type{margin-top:40px}
.contact b{font-weight:700}
.contact .hl{color:var(--red);font-size:15px}
.redline{position:absolute;left:0;top:2578px;width:1200px;height:4px;background:var(--red)}

/* footer */
.footer{position:absolute;left:0;top:2582px;width:1200px;height:262px;background:var(--black);color:var(--white)}
.f-contacts{position:absolute;top:44px;left:0;right:0;display:flex;justify-content:center;gap:54px;font-size:17px}
.f-contacts div{display:flex;align-items:center;gap:16px}
.circle{width:44px;height:44px;border-radius:50%;border:2px solid var(--white);display:flex;align-items:center;justify-content:center}
.circle svg{width:18px;height:18px;fill:var(--white)}
.f-nav{position:absolute;top:132px;left:0;right:0;display:flex;justify-content:center;gap:14px;font-size:15px;font-weight:600;text-transform:uppercase}
.f-nav .gap{margin-left:16px}
.copy{position:absolute;left:100px;top:206px;font-size:13px}
.social{position:absolute;right:100px;top:194px;display:flex;gap:10px}
.social span{width:36px;height:36px;border-radius:50%;border:2px solid var(--white)}
</style>
</head>
<body>

<header class="hero">
  <div class="hero-photo" role="img" aria-label="Night view of a floodlit cathedral above a city skyline"></div>
  <div class="topbar">
    <svg class="ico" viewBox="0 0 24 24"><path d="M6.6 10.8a15.1 15.1 0 0 0 6.6 6.6l2.2-2.2c.3-.3.7-.4 1-.2 1.1.4 2.3.6 3.6.6.6 0 1 .4 1 1V20c0 .6-.4 1-1 1A17 17 0 0 1 3 4c0-.6.4-1 1-1h3.5c.6 0 1 .4 1 1 0 1.3.2 2.5.6 3.6.1.3 0 .7-.2 1z"/></svg>
    <span>0700 555 0193</span><span class="sep">|</span>
    <svg class="ico" viewBox="0 0 24 24"><path d="M2 5h20v14H2z" fill="var(--red)"/><path d="M2 5l10 8 10-8" fill="none" stroke="#222" stroke-width="1.6"/></svg>
    <span>velmoraswingers@postwell.co.uk</span>
  </div>
  <div class="logo">VELMORA</div>
  <nav class="mainnav">
    <a>Home</a><a>Diary</a><a>Theme Parties</a><a>TV/TG and Admirers</a><a class="active">Membership</a><a>FAQs</a><a>Rooms</a><a>Contact Us</a><a>Links</a>
    <svg viewBox="0 0 16 16"><circle cx="6.5" cy="6.5" r="5"/><path d="M10.3 10.3L15 15"/></svg>
  </nav>
  <h1 class="hero-title">MEMBERSHIP</h1>
  <div class="dots"><span class="on"></span><span></span><span></span><span></span></div>
</header>

<main class="main">
  <div class="wrap crumb">Home &nbsp;&gt;&gt;&nbsp; <span class="cur">Membership</span></div>

  <section class="wrap intro">
    <h2>Velmora Membership</h2>
    <p>Sometimes we put new memberships on hold for certain categories, this is a private member's club and if we restrict membership it's for good reason, mainly to keep the balance right. If you already know a member you should ask them to introduce you, (ask them to call or message us so your name is on the guest list) or phone on the Velmora phone to arrange your first visit. The club phone is switched on from 2pm on the days we open (Wed/Fri/Sat). Its often answered at other times, but if you are already a member and want to book a room then just text. Single males can apply at the club on a Wednesday &amp; Friday. You must call us first so we can have a chat and put your name on the guest list. Please note guys, you cannot just turn up and expect to join.</p>
    <p>Membership cannot be guaranteed at any point. If you turn up drunk, scruffy or demanding to be let in (it does not happen often, but from time to time it does unfortunately happen) then it is likely you will not be allowed to join, it's also important that you understand what we say and can communicate well, people come to socialise and talk as well as to play. The Team Leader on duty can use their discretion regarding this. Membership cannot be guaranteed over the telephone. Please bring one form of ID each on your first visit as we CANNOT issue membership without this. We prefer a Driving License, we take a copy of all id, Passports are fine, but also need proof of address if you bring your passport, any other id must have your name and address on it, photo driving licenses are good. (We are fully licensed by the Data Office to keep members info, WE DO NOT SHARE YOUR INFORMATION WITH ANYONE)</p>
    <p>We do not accept applications from anyone under the age of 23 yrs. (Unless you are part of an established and verified couple, OR CAN BE FULLY VERIFIED AND ACCOMPANIED BY REGULAR ESTABLISHED MEMBERS, this is a discretionary management decision.)</p>
  </section>

  <div class="wrap divider"></div>

  <section class="wrap fees">
    <h2>Entry Fees</h2>
    <p class="price">£30.00 per couple or single guy (this includes half price entry for your next two visits)<br>£10.00 per single girl.</p>
    <p class="note">Military and Emergency Service Personnel, both serving &amp;retired (proof required) are always £15 membership, £10 renewal and half price entry. You must remind us though every time you come along. The hotel rooms and crash do not qualify for discounts.</p>
  </section>

  <section class="wrap plans">
    <svg width="0" height="0" style="position:absolute"><defs><symbol id="tick" viewBox="0 0 14 14"><circle cx="7" cy="7" r="7" fill="#e0262d"/><path d="M3.8 7.2l2.2 2.2 4.2-4.4" fill="none" stroke="#fff" stroke-width="1.8"/></symbol></defs></svg>
    <article class="plan">
      <div class="plan-box">
        <div class="plan-title">Greedy Girls</div>
        <div class="plan-time">Wednesday 8pm till Midnight</div>
        <ul>
          <li><svg><use href="#tick"/></svg>Single Girls are VIP guests tonight</li>
          <li><svg><use href="#tick"/></svg>Single guys £20,</li>
          <li><svg><use href="#tick"/></svg>Couples £15,</li>
          <li><svg><use href="#tick"/></svg>Greedy Girl Couples £10</li>
          <li><svg><use href="#tick"/></svg>(towels £2 each).</li>
        </ul>
      </div>
      <p class="plan-note">Wednesday night is a Greedy Girls night and there are no completely private rooms, if you wish to have privacy then we can hire you a hotel room (if any are available) which is £15 per couple for up to 1hr.</p>
      <p class="plan-note">Room &amp; entry on a Wednesday is £45 for a couple and £55 for a single guy, if you want to party on after closing then try this.....crash is £10 each plus your entry.</p>
    </article>
    <article class="plan featured">
      <div class="plan-box">
        <div class="plan-title">Mixed Night</div>
        <div class="plan-time">Friday Night - 8pm till 1.30am</div>
        <ul>
          <li><svg><use href="#tick"/></svg>Single Guys £22,</li>
          <li><svg><use href="#tick"/></svg>Single Girls £5,</li>
          <li><svg><use href="#tick"/></svg>Couples - £22,</li>
        </ul>
      </div>
      <p class="plan-note">Friday nights in the hotel, including your entry is £50 for a private room and £45 for a shared room or £10 per person for crash.</p>
    </article>
    <article class="plan">
      <div class="plan-box">
        <div class="plan-title">Couples Night</div>
        <div class="plan-time">Saturday night - 8pm till 1.30am</div>
        <p class="select">(Select single guys only)</p>
        <ul>
          <li><svg><use href="#tick"/></svg>Couples £25.00</li>
          <li><svg><use href="#tick"/></svg>Single girls £10.00</li>
          <li><svg><use href="#tick"/></svg>Select Single guys £35.00,</li>
          <li class="plain">(you must be pre booked).</li>
        </ul>
      </div>
      <p class="plan-note">Saturday nights in the hotel are £60 for a private room and £50 for a shared room (this includes entry) crash is £10 per person</p>
    </article>
  </section>
</main>

<section class="contact">
  <div class="contact-photo" role="img" aria-label="Dim club interior with draped curtains"></div>
  <h2>CONTACT US</h2>
  <p><b>PHONE -</b> If you are a new member and want to put your name on the guest list or ask a question, then call on that day after 2pm - <span class="hl">0700 555 0193</span>, if no answer - ring back.</p>
  <p><b>TEXT -</b> If you wish to book rooms or crash then text anytime and when we check the diary we will text you back to confirm your reservation. Please ensure you state your names, membership number if possible, the date you want to stay and if you want private, shared or crash. The phone is on Wed/Fri/Sat and often checked in between, but not 24/7 and sometimes the signal is bad... just keep on trying, it will be worth it!</p>
  <p><b>EMAIL -</b> The best way to contact Velmora is by phone, but we do respond to emails <span class="hl">velmoraswingers@postwell.co.uk</span>, though often not immediately, all room bookings and new members must go via the club phone.</p>
  <p><b>LUSH LINKS -</b> you can contact us by a few different Velmora profiles on lushlinks.com just put Velmora into the search bar.</p>
</section>
<div class="redline"></div>

<footer class="footer">
  <div class="f-contacts">
    <div><span class="circle"><svg viewBox="0 0 24 24"><path d="M6.6 10.8a15.1 15.1 0 0 0 6.6 6.6l2.2-2.2c.3-.3.7-.4 1-.2 1.1.4 2.3.6 3.6.6.6 0 1 .4 1 1V20c0 .6-.4 1-1 1A17 17 0 0 1 3 4c0-.6.4-1 1-1h3.5c.6 0 1 .4 1 1 0 1.3.2 2.5.6 3.6.1.3 0 .7-.2 1z"/></svg></span>0700 555 0193</div>
    <div><span class="circle"><svg viewBox="0 0 24 24"><path d="M2 5h20v14H2z"/><path d="M2 5l10 8 10-8" fill="none" stroke="#000" stroke-width="1.6"/></svg></span>velmoraswingers@postwell.co.uk</div>
  </div>
  <nav class="f-nav">
    <a>Home</a><a>Diary</a><a>Theme Parties</a><a class="gap">TV/TG and Admirers</a><a>Membership</a><a>FAQs</a><a>Rooms</a><a>Contact Us</a><a>Links</a>
  </nav>
  <p class="copy">Copyrights © 2017, Velmora. All rights reserved.</p>
  <div class="social"><span></span><span></span><span></span></div>
</footer>

</body>
</html>
```